Kestrel Valley Alpine Riders Society needs a business card design

We need a business card design for our newly incorporated KVARS. We are helping the NZ Chinese community, as well as everyone else, to organise ski & snowboarding trips, training, and equipments. The design should be creative, energetic, young and vibrant.

Industry/Entity Type

Social Club

Contact Information for Business Card

Logo; Kestrel Valley Alpine Riders Society; Name: Oliver Brandt; Position: President; Address: 42 Marwick Rd, Epsom, Auckland 1051; Mobile: 020 7826 1957; Email: oliver@kvars-club.example; Web: www.kvars-club.example

Requirements
Must have
• 1, The text "Kestrel Valley Alpine Riders Society" should be put together with the supplied logo file to form a new complete logo combination.
• 2, Final design files should be in Adobe Illustrator format and all text must be editable.
Nice to have
• two or three colours

```html
<!DOCTYPE html>
<html lang="en">
<head>
<meta charset="utf-8">
<title>Kestrel Valley Alpine Riders Society – Business Card</title>
<link rel="stylesheet" href="https://fonts.googleapis.com/css2?family=Roboto:wght@400;500;700&display=swap">
<style>
  :root {
    --navy: #28317a;
    --navy-back: #263377;
    --ink: #4d4f55;
    --sky: #3e9be0;
    --ice: #5fb8f0;
    --paper: #ffffff;
    --stage: #eceef2;
  }
  * { box-sizing: border-box; margin: 0; padding: 0; }
  html, body {
    width: 1200px; height: 1200px; overflow: hidden;
    background: var(--stage);
    font-family: "Roboto", Arial, sans-serif;
  }
  .canvas { position: relative; width: 1200px; height: 1200px; }
  .card {
    position: absolute; left: 213px; width: 774px; height: 441px;
    overflow: hidden;
  }
  .card--front { top: 150px; background: var(--paper); }
  .card--back { top: 634px; background: var(--navy-back); }

  .front-brand {
    position: absolute; left: 70px; top: 170px; width: 280px;
    display: flex; align-items: center; justify-content: center; gap: 12px;
  }
  .brand-dot { width: 22px; height: 22px; border-radius: 50%; background: var(--sky); }
  .brand-name { font-weight: 700; font-size: 56px; color: var(--navy); letter-spacing: 1px; line-height: 1; }

  .divider { position: absolute; left: 390px; top: 113px; width: 2px; height: 215px; background: var(--navy); }

  .contact { position: absolute; left: 423px; top: 106px; color: var(--ink); }
  .contact__name { font-weight: 500; font-size: 28px; color: var(--navy); line-height: 1.1; letter-spacing: 0.5px; }
  .contact__role { font-size: 20px; line-height: 1.4; }
  .contact__address { margin-top: 22px; font-size: 20px; line-height: 28px; }
  .contact__list { margin-top: 14px; list-style: none; font-size: 20px; line-height: 27px; }
  .contact__list li { display: flex; align-items: center; gap: 6px; }
  .contact__list svg { width: 18px; height: 18px; flex: none; }

  .name-band {
    position: absolute; left: 0; bottom: 0; width: 100%; height: 40px;
    background: var(--navy); color: #fff; font-size: 18px;
    display: flex; align-items: center; justify-content: center;
  }

  .back-brand {
    position: absolute; inset: 0;
    display: flex; flex-direction: column; align-items: center; justify-content: center; gap: 14px;
  }
  .back-brand__row { display: flex; align-items: center; gap: 22px; }
  .back-brand__dot { width: 40px; height: 40px; border-radius: 50%; background: var(--ice); }
  .back-brand__name { font-weight: 700; font-size: 120px; line-height: 1; color: var(--ice); letter-spacing: 3px; }
  .back-brand__full { font-weight: 500; font-size: 18px; color: #fff; }
</style>
</head>
<body>
<div class="canvas">
  <section class="card card--front">
    <div class="front-brand">
      <span class="brand-dot"></span>
      <span class="brand-name">KVARS</span>
    </div>
    <div class="divider"></div>
    <div class="contact">
      <p class="contact__name">OLIVER BRANDT</p>
      <p class="contact__role">President</p>
      <p class="contact__address">42 Marwick Rd<br>Epsom, Auckland 1051</p>
      <ul class="contact__list">
        <li>
          <svg viewBox="0 0 18 18" fill="none" stroke="var(--sky)" stroke-width="1.5"><rect x="4.5" y="1.5" width="9" height="15" rx="1.5"/><line x1="8" y1="14" x2="10" y2="14"/></svg>
          020 7826 1957
        </li>
        <li>
          <svg viewBox="0 0 18 18" fill="none" stroke="var(--sky)" stroke-width="1.5"><rect x="1.5" y="4" width="15" height="10" rx="1"/><polyline points="1.5,4.5 9,10 16.5,4.5"/></svg>
          oliver@kvars-club.example
        </li>
        <li>
          <svg viewBox="0 0 18 18" fill="none" stroke="var(--sky)" stroke-width="1.4"><circle cx="9" cy="9" r="7"/><ellipse cx="9" cy="9" rx="3" ry="7"/><line x1="2" y1="9" x2="16" y2="9"/><line x1="3" y1="5.5" x2="15" y2="5.5"/><line x1="3" y1="12.5" x2="15" y2="12.5"/></svg>
          www.kvars-club.example
        </li>
      </ul>
    </div>
    <div class="name-band">Kestrel Valley Alpine Riders Society</div>
  </section>

  <section class="card card--back">
    <div class="back-brand">
      <div class="back-brand__row">
        <span class="back-brand__dot"></span>
        <span class="back-brand__name">KVARS</span>
      </div>
      <p class="back-brand__full">Kestrel Valley Alpine Riders Society</p>
    </div>
  </section>
</div>
</body>
</html>
```